Beyond the Hunt Product Labeling

We need a label design for a new product we are launching. We have developed a cooking bag that will cook your fish or game bird instantly. This is for the everyday fisherman and upland game hunter. This label will be printed on a thin sticker on the front of a Mylar Bag. The Mylar Bag is 9 1/2 x 12 inches. Inside the Mylar Bag is 3 cooking bags.
Target Market(s)
hunters and fishermen
Industry/Entity Type
Cooking
Font styles to use
Sans Serif
Colors
Designer to choose colors to be used in the design.
Requirements
Must have
- It must have "Beyond the Hunt" logo. It should have Scale and Plume. Scale and Plume is the type of seasoning. It must have a small place on the label for net weight. It must also have the wording "Contains: 3 Individual Cooking Bags Inside.
Nice to have
- I really like a topographical map in the background. I have attached several images with products like that. It could also be cool having the background of the bag with a tiger trout's scales. I attached some images of that too. Some other ideas I thought i have is having a picture of the bird and fish on the bag. There is an GIF attached that has a cool looking fish that did that. There is also an image of a Holvak product that did the same thing.

```html
<!DOCTYPE html>
<html lang="en">
<head>
<meta charset="utf-8">
<title>Beyond the Hunt – Cooking Bag Label</title>
<link href="https://fonts.googleapis.com/css2?family=Bebas+Neue&family=Lato:wght@700;900&display=swap" rel="stylesheet">
<style>
  :root {
    --frame: #3a3a3a;
    --ink: #000000;
    --paper: #ffffff;
    --topo-light: #f7f7f7;
    --topo-mid: #cfcfcf;
    --art-tone: #d9d9d9;
  }
  html, body {
    margin: 0;
    padding: 0;
    width: 974px;
    height: 1200px;
    overflow: hidden;
    background: var(--frame);
  }
  .label {
    position: relative;
    width: 974px;
    height: 1200px;
    background: var(--frame);
  }
  .label__field {
    position: absolute;
    left: 62px;
    top: 62px;
    width: 850px;
    height: 1076px;
    background:
      radial-gradient(ellipse at 12% 30%, var(--topo-mid) 0%, transparent 45%),
      radial-gradient(ellipse at 90% 70%, var(--topo-mid) 0%, transparent 45%),
      radial-gradient(ellipse at 50% 100%, #dadada 0%, transparent 55%),
      var(--topo-light);
  }
  .label__pennant {
    position: absolute;
    left: 0;
    top: 0;
    width: 974px;
    height: 1200px;
  }
  .art {
    position: absolute;
    border-radius: 8px;
    background: linear-gradient(135deg, #ececec, var(--art-tone));
    opacity: 0.9;
  }
  .art--elk-range {
    left: 204px;
    top: 132px;
    width: 460px;
    height: 200px;
  }
  .art--fish-bird {
    left: 228px;
    top: 472px;
    width: 540px;
    height: 156px;
  }
  .brand-name {
    position: absolute;
    right: 198px;
    top: 346px;
    margin: 0;
    font-family: "Bebas Neue", "Oswald", sans-serif;
    font-weight: 400;
    font-size: 80px;
    line-height: 1;
    letter-spacing: 0.5px;
    color: var(--paper);
    white-space: nowrap;
  }
  .rule {
    position: absolute;
    left: 210px;
    width: 552px;
    height: 2px;
    background: var(--paper);
  }
  .rule--top { top: 638px; }
  .rule--bottom { top: 766px; }
  .contents {
    position: absolute;
    left: 182px;
    width: 612px;
    top: 672px;
    margin: 0;
    text-align: center;
    font-family: "Lato", sans-serif;
    font-weight: 700;
    font-size: 21px;
    line-height: 1.35;
    color: var(--paper);
    text-transform: uppercase;
  }
  .seasoning {
    position: absolute;
    left: 182px;
    width: 612px;
    top: 790px;
    margin: 0;
    text-align: center;
    font-family: "Bebas Neue", "Oswald", sans-serif;
    font-weight: 400;
    font-size: 44px;
    line-height: 1;
    letter-spacing: 1px;
    color: var(--paper);
  }
  .net-weight {
    position: absolute;
    left: 182px;
    width: 612px;
    top: 870px;
    margin: 0;
    text-align: center;
    font-family: "Lato", sans-serif;
    font-weight: 700;
    font-size: 22px;
    line-height: 1.45;
    color: var(--paper);
  }
</style>
</head>
<body>
  <main class="label">
    <div class="label__field" role="img" aria-label="Topographic contour map pattern in black line on white"></div>

    <svg class="label__pennant" viewBox="0 0 974 1200" aria-hidden="true">
      <path d="M166,62 L810,62 L810,850 Q810,862 798,870 L500,1034 Q488,1041 476,1034 L178,870 Q166,862 166,850 Z"
            fill="var(--paper)" stroke="var(--ink)" stroke-width="4"/>
      <path d="M182,62 L794,62 L794,838 Q794,848 784,854 L498,1012 Q488,1018 478,1012 L192,854 Q182,848 182,838 Z"
            fill="var(--ink)"/>
    </svg>

    <div class="art art--elk-range" role="img" aria-label="Illustration of a bugling elk head with antlers beside a mountain ridge"></div>

    <h1 class="brand-name">BEYOND THE HUNT</h1>

    <div class="art art--fish-bird" role="img" aria-label="Illustration of a leaping trout facing a perched upland game bird silhouette"></div>

    <div class="rule rule--top"></div>
    <p class="contents">Contains:<br>3 Individual Cooking Bags Inside</p>
    <div class="rule rule--bottom"></div>

    <p class="seasoning">Scale and Plume</p>

    <p class="net-weight">Net Weight<br>75gm oz</p>
  </main>
</body>
</html>
```